Paper and board wholesaler needs business card design for managers

We need a business card design that incorporates bordo red, white and/ or grey colors. The business card has to have our "VELON" logo and our partners paper group logo that we are part of - "ROSKU group". Both of the logos should be applied to the business card according to the guidelines for the usage of the logo that have been added in the uploaded files.
The letters (information on the card) should be easily readable, so no "shiny" or "glossy" text.
Besides the two logos, the business card needs to contain information for the respective person:
1) Name, Surname,
2) Job position (e.g. "sales represantative"),
3) E-mail,
4) Phone number,
5) text: "Kartonu Mājvieta (VELON)" LTD
6) our office address "Riga, Sārtaines street 42".
(also could have) 7) our homepage address "www.velon.lv"
Holiday season, so have a lot of tasks to take care of and not as much time to check SketchHarbor as often.
1) Name, Surname, 2) Job position (e.g. "sales represantative"), 3) E-mail, 4) Phone number, 5) text: "Kartonu Mājvieta (VELON)" LTD 6) our office address "Riga, Sārtaines street 42". (also could have) 7) our homepage address "www.velon.lv"
Other font styles liked:
- Josefin Sans

```html
<!DOCTYPE html>
<html lang="en">
<head>
<meta charset="UTF-8">
<title>VELON business cards</title>
<link rel="stylesheet" href="https://fonts.googleapis.com/css2?family=Josefin+Sans:wght@300;400;600&display=swap">
<style>
  :root {
    --bordo: #822f35;
    --charcoal: #2e2e2f;
    --paper: #ffffff;
    --backdrop: #e3e4e6;
    --ink-light: #ffffff;
  }
  * { margin: 0; padding: 0; box-sizing: border-box; }
  html, body {
    width: 900px; height: 1200px; overflow: hidden;
    background: var(--backdrop);
    font-family: "Josefin Sans", sans-serif;
  }
  .canvas {
    position: relative; width: 900px; height: 1200px;
    display: flex; justify-content: center; align-items: center; gap: 36px;
  }
  .card {
    position: relative; width: 340px; height: 590px; overflow: hidden;
  }

  /* Front: bordo */
  .card--front { background: var(--bordo); color: var(--ink-light); }
  .group-mark {
    position: absolute; top: 48px; left: 0; width: 100%;
    display: flex; justify-content: center; align-items: center; gap: 8px;
  }
  .group-mark__dot {
    width: 22px; height: 22px; border: 2px solid var(--ink-light); border-radius: 50%;
  }
  .group-mark__name { font-weight: 600; font-size: 21px; letter-spacing: 0.5px; line-height: 1; padding-top: 3px; }
  .brand-mark--front {
    position: absolute; left: 95px; top: 218px; width: 150px; height: 150px;
    border: 6px solid var(--ink-light); border-radius: 50%;
  }
  .brand-name--front {
    position: absolute; top: 496px; width: 100%; text-align: center;
    font-weight: 400; font-size: 31px; letter-spacing: 22px; padding-left: 22px;
  }

  /* Back: contact */
  .card--back { background: var(--paper); }
  .card-bands { position: absolute; inset: 0; }
  .brand-lockup--back {
    position: absolute; top: 86px; left: 26px;
    display: flex; align-items: center; gap: 44px;
  }
  .brand-mark--back {
    width: 52px; height: 52px; border: 3px solid var(--bordo); border-radius: 50%;
  }
  .brand-name--back {
    font-weight: 400; font-size: 26px; letter-spacing: 16px; color: var(--bordo);
    line-height: 1; padding-top: 4px;
  }
  .person {
    position: absolute; left: 42px; top: 326px; color: var(--ink-light);
  }
  .person-name { font-weight: 600; font-size: 25px; letter-spacing: 0.5px; line-height: 1.2; }
  .person-role { font-weight: 400; font-size: 18px; line-height: 1.2; }
  .contact-list { list-style: none; margin-top: 20px; }
  .contact-item {
    display: flex; align-items: center; gap: 9px;
    font-weight: 400; font-size: 17px; height: 29px;
  }
  .contact-item svg { width: 14px; height: 14px; flex: none; }
  .office-address { font-size: 17px; margin-top: 16px; }
  .company-legal { font-size: 14px; margin-top: 10px; opacity: 0.9; }
</style>
</head>
<body>
<main class="canvas">
  <section class="card card--front">
    <div class="group-mark">
      <span class="group-mark__dot" aria-hidden="true"></span>
      <span class="group-mark__name">ROSKU group</span>
    </div>
    <div class="brand-mark--front" role="img" aria-label="VELON brand mark placeholder"></div>
    <div class="brand-name--front">VELON</div>
  </section>

  <section class="card card--back">
    <svg class="card-bands" viewBox="0 0 340 590" preserveAspectRatio="none" aria-hidden="true">
      <polygon points="0,290 340,212 340,230 0,313" fill="var(--bordo)"/>
      <polygon points="0,313 340,230 340,590 0,590" fill="var(--charcoal)"/>
    </svg>
    <div class="brand-lockup--back">
      <span class="brand-mark--back" aria-hidden="true"></span>
      <span class="brand-name--back">VELON</span>
    </div>
    <div class="person">
      <div class="person-name">YOUR NAME</div>
      <div class="person-role">Job Position</div>
      <ul class="contact-list">
        <li class="contact-item">
          <svg viewBox="0 0 24 24" aria-hidden="true"><path fill="#fff" d="M6.6 10.8a15.1 15.1 0 0 0 6.6 6.6l2.2-2.2c.3-.3.7-.4 1-.2 1.1.4 2.3.6 3.6.6.6 0 1 .4 1 1V20c0 .6-.4 1-1 1A17 17 0 0 1 3 4c0-.6.4-1 1-1h3.5c.6 0 1 .4 1 1 0 1.3.2 2.5.6 3.6.1.3 0 .7-.2 1z"/></svg>
          012 345 6789
        </li>
        <li class="contact-item">
          <svg viewBox="0 0 24 24" aria-hidden="true"><rect x="2" y="5" width="20" height="14" fill="#fff"/><path d="M2 5l10 8 10-8" fill="none" stroke="var(--charcoal)" stroke-width="1.8"/></svg>
          Yourmail@velonmail.lv
        </li>
        <li class="contact-item">
          <svg viewBox="0 0 24 24" aria-hidden="true"><g fill="none" stroke="#fff" stroke-width="2"><circle cx="12" cy="12" r="9.5"/><ellipse cx="12" cy="12" rx="4" ry="9.5"/><path d="M2.5 12h19"/></g></svg>
          www.velon.lv
        </li>
      </ul>
      <div class="office-address">Riga, Sārtaines street 42</div>
      <div class="company-legal">“Kartonu Mājvieta (VELON)” LTD</div>
    </div>
  </section>
</main>
</body>
</html>
```